New Business Card Design*

We are a recruitment company based in Norwich/Cambridge England.
I have included our company logo which we want to remain the same.

What we are looking for is a new creative Business card which will really stand out!!

Contact Information for Business Card

Harriet Dunmore
email: Harriet@vexalim.co.uk
Address: Larkwell House
Brambleton Enterprise Quarter
Thistlebrook Road
Norwich
QX9 2LB
Tel:01632 418305

```html
<!DOCTYPE html>
<html lang="en">
<head>
<meta charset="utf-8">
<title>Vexalim Business Card</title>
<link rel="stylesheet" href="https://fonts.googleapis.com/css2?family=Nunito:wght@400;600;800&display=swap">
<style>
  :root {
    --backdrop: #161719;
    --card: #222523;
    --card-edge: #2b2f2c;
    --green: #7ac943;
    --grey: #9a989e;
    --text: #b9babc;
  }
  * { margin: 0; padding: 0; box-sizing: border-box; }
  html, body { width: 1200px; height: 800px; overflow: hidden; background: var(--backdrop); }
  body { font-family: "Nunito", sans-serif; position: relative; }

  .card {
    position: absolute;
    width: 520px;
    height: 300px;
    background: var(--card);
    border: 1px solid var(--card-edge);
    border-radius: 4px;
    box-shadow: 0 18px 40px rgba(0,0,0,0.55);
    overflow: hidden;
  }
  .card--front { left: 70px; top: 110px; }
  .card--back { left: 610px; top: 390px; }

  .brand { display: flex; align-items: center; gap: 14px; }
  .brand__dot {
    width: 44px; height: 44px; border-radius: 50%;
    background: var(--green);
  }
  .brand__name {
    font-weight: 800; font-size: 46px; line-height: 1;
    color: var(--green); letter-spacing: -0.5px;
  }
  .brand__tagline {
    font-size: 10px; letter-spacing: 3.2px; color: var(--text);
    text-transform: none; margin-top: 4px;
  }
  .card--front .brand {
    position: absolute; left: 50%; top: 50%;
    transform: translate(-50%, -50%);
  }

  .card--back .brand { position: absolute; left: 36px; top: 30px; }
  .card--back .brand__dot { width: 34px; height: 34px; }
  .card--back .brand__name { font-size: 36px; }
  .card--back .brand__tagline { font-size: 8.5px; letter-spacing: 2.6px; }

  .holder { position: absolute; left: 36px; top: 112px; }
  .holder__name { font-weight: 800; font-size: 20px; color: var(--green); line-height: 1.1; }
  .holder__role { font-size: 12px; color: var(--text); letter-spacing: 0.5px; }

  .address {
    position: absolute; left: 36px; top: 170px;
    font-size: 11px; line-height: 1.45; color: var(--text); font-style: normal;
  }

  .contacts {
    position: absolute; right: 32px; top: 180px;
    list-style: none; font-size: 11.5px; color: var(--text);
  }
  .contacts__item { display: flex; align-items: center; gap: 9px; margin-bottom: 9px; }
  .contacts__icon { width: 18px; height: 18px; flex: none; }
</style>
</head>
<body>

  <section class="card card--front" aria-label="Card front">
    <div class="brand">
      <span class="brand__dot"></span>
      <div>
        <div class="brand__name">Vexalim</div>
        <div class="brand__tagline">Technology Recruitment</div>
      </div>
    </div>
  </section>

  <section class="card card--back" aria-label="Card back">
    <div class="brand">
      <span class="brand__dot"></span>
      <div>
        <div class="brand__name">Vexalim</div>
        <div class="brand__tagline">Technology Recruitment</div>
      </div>
    </div>

    <div class="holder">
      <div class="holder__name">Harriet Dunmore</div>
      <div class="holder__role">CEO</div>
    </div>

    <address class="address">
      Larkwell House<br>
      Brambleton Enterprise Quarter<br>
      Thistlebrook Road<br>
      Norwich<br>
      QX9 2LB
    </address>

    <ul class="contacts">
      <li class="contacts__item">
        <svg class="contacts__icon" viewBox="0 0 18 18" aria-hidden="true">
          <circle cx="9" cy="9" r="8" fill="none" stroke="#7ac943" stroke-width="1.4"/>
          <rect x="6.2" y="4.2" width="5.6" height="9.6" rx="1" fill="none" stroke="#7ac943" stroke-width="1.2"/>
          <circle cx="9" cy="12" r="0.6" fill="#7ac943"/>
        </svg>
        01632 418305
      </li>
      <li class="contacts__item">
        <svg class="contacts__icon" viewBox="0 0 18 18" aria-hidden="true">
          <circle cx="9" cy="9" r="8" fill="none" stroke="#7ac943" stroke-width="1.4"/>
          <rect x="4.5" y="6" width="9" height="6.2" fill="none" stroke="#7ac943" stroke-width="1.2"/>
          <path d="M4.5 6 L9 9.6 L13.5 6" fill="none" stroke="#7ac943" stroke-width="1.2"/>
        </svg>
        Harriet@vexalim.co.uk
      </li>
      <li class="contacts__item">
        <svg class="contacts__icon" viewBox="0 0 18 18" aria-hidden="true">
          <circle cx="9" cy="9" r="8" fill="none" stroke="#7ac943" stroke-width="1.4"/>
          <circle cx="9" cy="9" r="4.6" fill="none" stroke="#7ac943" stroke-width="1.1"/>
          <ellipse cx="9" cy="9" rx="2" ry="4.6" fill="none" stroke="#7ac943" stroke-width="1"/>
          <line x1="4.4" y1="9" x2="13.6" y2="9" stroke="#7ac943" stroke-width="1"/>
        </svg>
        vexalim.co.uk
      </li>
    </ul>
  </section>

</body>
</html>
```